Corporate Letter head and Microsoft Word Template

Brief
Design three clean, modern, professional corporate letter templates that include the BrightArc Corporation word-mark logo, company name and address and url. The designs should use one or more but no more than three tints/shades from our corporate colour pallet.
Templates should be produced in A4 and Letter formats as a Word file and should use Helvetica Now Display as the embedded font.
Design Preference:
Colour block designs, solid borders with flowing smooth lines, single side borders with connected header and footer, cut off or half page headers and footers are all acceptable.
Deliverables are:
1. Three graphic design files one for each brand logo colour and design
2. Three Word templates in 2 formats A4 and Letter
Enclosed are:
1. Three word mark logos with reverse versions of each, one for each primary brand colour.
2. BrightArc corporate colour pallet
3. BrightArc address and url
4. Helvetica Now Display font files

Target Market(s)

Professional Letter Writing to Suppliers, Customers and Authorities

Industry/Entity Type

High Tech

Font styles to use
Sans Serif
Other font styles liked:
• Helvetica Now Display

Requirements
Must have
• Clean, modern and effective design incorporating BrightArc Wordmark logo

```html
<!DOCTYPE html>
<html lang="en">
<head>
<meta charset="utf-8">
<title>BrightArc Corporation – Letterhead</title>
<link rel="stylesheet" href="https://fonts.googleapis.com/css2?family=Inter:wght@400;500;600;800&display=swap">
<style>
  :root {
    --brand-orange: #fc4a05;
    --brand-peach: #f5a281;
    --brand-rust: #a52f21;
    --rule-coral: #f27a5a;
    --ink: #111111;
    --paper: #fefefe;
    --white: #ffffff;
  }
  * { margin: 0; padding: 0; box-sizing: border-box; }
  html, body { width: 849px; height: 1200px; overflow: hidden; background: var(--paper); }
  body { font-family: "Inter", Helvetica, Arial, sans-serif; color: var(--ink); }

  .letterhead { position: relative; width: 849px; height: 1200px; background: var(--paper); }

  .wordmark {
    position: absolute;
    left: 68px;
    top: 80px;
    font-size: 50px;
    font-weight: 800;
    letter-spacing: -2px;
    line-height: 1;
    color: var(--brand-orange);
  }

  .company-address {
    position: absolute;
    left: 579px;
    top: 56px;
    font-size: 14px;
    line-height: 17px;
    letter-spacing: -0.3px;
    font-style: normal;
  }
  .company-address .company-name { font-weight: 600; font-size: 15px; }

  .header-rule {
    position: absolute;
    left: 68px;
    top: 140px;
    width: 763px;
    height: 1px;
    background: var(--rule-coral);
  }

  .footer-bands {
    position: absolute;
    left: 0;
    bottom: 0;
    width: 849px;
    height: 42px;
    display: flex;
  }
  .footer-bands .band { flex: 1; display: flex; align-items: center; justify-content: center; }
  .band--peach { background: var(--brand-peach); }
  .band--orange { background: var(--brand-orange); }
  .band--rust { background: var(--brand-rust); }
  .website { color: var(--white); font-size: 14px; letter-spacing: -0.2px; }
</style>
</head>
<body>
  <main class="letterhead">
    <div class="wordmark">BrightArc</div>

    <address class="company-address">
      <div class="company-name">BrightArc Corporation</div>
      <div>4870 NW Meridian Way, Suite 210,</div>
      <div>Portland, OR 97229</div>
      <div>United States</div>
    </address>

    <div class="header-rule"></div>

    <footer class="footer-bands">
      <div class="band band--peach"></div>
      <div class="band band--orange"><span class="website">brightarc.com</span></div>
      <div class="band band--rust"></div>
    </footer>
  </main>
</body>
</html>
```